Business Card Design

Mortgage brokering company, also providing Commercial Finance, Car Finance and Insurance.

Target Market(s)

Home Buyers

Industry/Entity Type

Business

Contact Information for Business Card

All information required on business card is contained in the attachment. Design does not have to follow the style of the attachment.

```html
<!DOCTYPE html>
<html lang="en">
<head>
<meta charset="utf-8">
<title>Harbourline Mortgage Services – Business Card</title>
<link rel="stylesheet" href="https://fonts.googleapis.com/css2?family=Source+Sans+3:ital,wght@0,300;0,400;0,700;1,400&display=swap">
<style>
  :root {
    --backdrop: #2b2b2d;
    --card-white: #fbfbfb;
    --card-silver: #e4e3e6;
    --band-grey: #bdbcc0;
    --band-light: #d2d1d5;
    --ink-navy: #2c3a4e;
    --ink-soft: #5b6577;
    --accent-orange: #ec7a22;
    --divider: #54627a;
  }
  * { box-sizing: border-box; margin: 0; padding: 0; }
  html, body {
    width: 1200px; height: 900px; overflow: hidden;
    background: var(--backdrop);
    font-family: "Source Sans 3", Arial, sans-serif;
  }
  .canvas { position: relative; width: 1200px; height: 900px; }

  .card {
    position: absolute;
    width: 560px; height: 320px;
    box-shadow: 0 18px 40px rgba(0,0,0,0.55);
    overflow: hidden;
  }

  /* Front: brand side */
  .card--brand {
    left: 110px; top: 120px;
    background: linear-gradient(135deg, var(--card-white) 0%, var(--card-silver) 100%);
    display: flex; flex-direction: column; align-items: center; justify-content: center;
  }
  .brand-lockup { display: flex; align-items: center; gap: 14px; }
  .brand-dot {
    width: 30px; height: 30px; border-radius: 50%;
    background: var(--accent-orange);
  }
  .brand-name {
    font-weight: 300; font-size: 30px; color: var(--ink-navy);
    letter-spacing: 0.5px;
  }
  .brand-web {
    margin-top: 26px;
    font-size: 12px; font-weight: 300; color: var(--ink-soft);
    letter-spacing: 4px;
  }

  /* Back: contact side */
  .card--contact {
    left: 530px; top: 480px;
    background: var(--card-white);
  }
  .contact-band {
    position: absolute; left: 0; right: 0; top: 88px; height: 150px;
    background: linear-gradient(90deg, var(--band-grey) 0%, var(--band-grey) 52%, var(--band-light) 52%, var(--band-light) 100%);
  }
  .contact-details {
    position: absolute; left: 36px; top: 108px; width: 250px;
    color: var(--ink-navy);
  }
  .contact-name { font-weight: 700; font-size: 19px; }
  .contact-role { font-style: italic; font-weight: 400; font-size: 13px; }
  .contact-list { list-style: none; margin-top: 12px; font-size: 11.5px; line-height: 1.45; }
  .contact-divider {
    position: absolute; left: 300px; top: 96px; width: 1px; height: 110px;
    background: var(--divider);
  }
  .contact-brand {
    position: absolute; left: 320px; top: 88px; width: 240px; height: 150px;
    display: flex; align-items: center; justify-content: center; gap: 10px;
  }
  .contact-brand .brand-dot { width: 22px; height: 22px; }
  .contact-brand .brand-name { font-size: 20px; }
</style>
</head>
<body>
  <main class="canvas">
    <section class="card card--brand">
      <div class="brand-lockup">
        <span class="brand-dot"></span>
        <span class="brand-name">Harbourline Mortgage Services</span>
      </div>
      <p class="brand-web">www.harbourlinemortgage.com.au</p>
    </section>

    <section class="card card--contact">
      <div class="contact-band"></div>
      <div class="contact-details">
        <p><span class="contact-name">Alex Morgan</span> <span class="contact-role">– Credit representative</span></p>
        <ul class="contact-list">
          <li>Adress: 14 Ocean Vale, Coral Heads, Qld 4299</li>
          <li>Mobile: 0400123456</li>
          <li>Phone/Fax: 0755501234</li>
          <li>Email: alex.morgan@harbourlinemortgage.com.au</li>
        </ul>
      </div>
      <div class="contact-divider"></div>
      <div class="contact-brand">
        <span class="brand-dot"></span>
        <span class="brand-name">Harbourline</span>
      </div>
    </section>
  </main>
</body>
</html>
```